Business Card For Quillmoor Financial Consulting

Hi, I would like a business card designed. Bold, modern.
Please use the same design as the logo. I have also attached the website design to see the overall theme.
Wordmark Font
Color: Hex: #01AEF7

```html
<!DOCTYPE html>
<html lang="en">
<head>
<meta charset="utf-8">
<title>Quillmoor Financial Consulting – Business Card</title>
<link rel="stylesheet" href="https://fonts.googleapis.com/css2?family=Montserrat:wght@400;500;700&display=swap">
<style>
  :root {
    --backdrop: #3b3b3b;
    --card: #17222d;
    --card-edge: #01aef7;
    --accent: #01aef7;
    --accent-soft: #3b9fd8;
    --text-light: #e9eef2;
    --emboss: #22303d;
  }
  * { margin: 0; padding: 0; box-sizing: border-box; }
  html, body {
    width: 1200px; height: 801px; overflow: hidden;
    background: var(--backdrop);
    font-family: "Montserrat", Arial, sans-serif;
  }
  .stage { position: relative; width: 1200px; height: 801px; }
  .card {
    position: absolute;
    width: 525px; height: 300px;
    background: var(--card);
    border-bottom: 3px solid var(--card-edge);
    box-shadow: 0 12px 28px rgba(0,0,0,.35);
  }
  .card--front { left: 60px; top: 110px; }
  .card--back { left: 615px; top: 390px; }

  .brand { position: absolute; left: 40px; top: 70px; display: flex; align-items: center; gap: 14px; }
  .brand__mark { width: 30px; height: 30px; border: 3px solid var(--accent); }
  .brand__name {
    color: var(--text-light); font-weight: 700; font-size: 22px;
    letter-spacing: 1px; text-transform: uppercase; line-height: 1.15;
  }

  .details { position: absolute; left: 40px; top: 175px; display: flex; align-items: center; }
  .person { width: 200px; text-align: right; padding-right: 22px; }
  .person__name { color: var(--accent); font-weight: 700; font-size: 20px; text-transform: uppercase; letter-spacing: .5px; }
  .person__role { color: var(--text-light); font-size: 14px; margin-top: 4px; }
  .divider { width: 1px; height: 72px; background: var(--accent); }
  .contacts { list-style: none; padding-left: 22px; }
  .contacts li {
    display: flex; align-items: center; gap: 10px;
    color: var(--text-light); font-size: 13px; line-height: 24px;
  }
  .contacts svg { width: 13px; height: 13px; fill: var(--accent); flex: none; }

  .back-brand {
    position: absolute; inset: 0;
    display: flex; align-items: center; justify-content: center; gap: 18px;
  }
  .back-brand__mark { width: 44px; height: 44px; border: 4px solid var(--emboss); }
  .back-brand__name {
    color: var(--emboss); font-weight: 700; font-size: 28px;
    letter-spacing: 1px; text-transform: uppercase; line-height: 1.15;
    text-shadow: 0 1px 0 rgba(255,255,255,.05);
  }
</style>
</head>
<body>
<main class="stage">
  <section class="card card--front">
    <div class="brand">
      <span class="brand__mark"></span>
      <span class="brand__name">Quillmoor<br>Financial Consulting</span>
    </div>
    <div class="details">
      <div class="person">
        <p class="person__name">Elena Marsh</p>
        <p class="person__role">Founder</p>
      </div>
      <span class="divider"></span>
      <ul class="contacts">
        <li><svg viewBox="0 0 24 24"><path d="M6.6 10.8a15 15 0 0 0 6.6 6.6l2.2-2.2c.3-.3.7-.4 1-.2 1.1.4 2.3.6 3.6.6.6 0 1 .4 1 1V20c0 .6-.4 1-1 1A17 17 0 0 1 3 4c0-.6.4-1 1-1h3.5c.6 0 1 .4 1 1 0 1.3.2 2.5.6 3.6.1.3 0 .7-.2 1z"/></svg>555-014-2280</li>
        <li><svg viewBox="0 0 24 24"><path d="M2 5h20v14H2zm2 2v.5l8 5 8-5V7z"/></svg>info@quillmoorconsulting.com</li>
        <li><svg viewBox="0 0 24 24"><circle cx="12" cy="12" r="10"/></svg>www.Quillmoorconsulting.com</li>
      </ul>
    </div>
  </section>

  <section class="card card--back">
    <div class="back-brand">
      <span class="back-brand__mark"></span>
      <span class="back-brand__name">Quillmoor<br>Financial Consulting</span>
    </div>
  </section>
</main>
</body>
</html>
```